Book cover design for a collection of poetry - The Lanternfield

Book cover and back design need to be moody, nostalgic, reflective, ethereal. Melancholy and other worldly. Cover design should not be time specific to a period or place but if applicable should reflect British landscape. Book cover should be in tones of blue and must include the title and author (THE LANTERNFIELD BY DORIAN WELKBRIDGE). We love the idea of rain, and looking out of a window. See attached designs. A world you are observing but not in.

Industry/Entity Type

Book Publisher

Font styles to use
Serif
Script

Colors
3176b5
3377b5
85acd3
eaf1f7
0792cd
33a6d7
86cae7
ecf7fb
86cfc6

Requirements
Must have
• The colour blue in it, must be melancholy and reflective.
Nice to have
• Rain in the cover.
Should not have
• Any bright colours.

```html
<!DOCTYPE html>
<html lang="en">
<head>
<meta charset="utf-8">
<title>The Lanternfield – Cover Spread</title>
<link rel="stylesheet" href="https://fonts.googleapis.com/css2?family=Sorts+Mill+Goudy:ital@0;1&family=Old+Standard+TT:wght@400&family=Barlow:wght@400&family=Crimson+Text:wght@400;700&display=swap">
<style>
  :root {
    --page: #ffffff;
    --teal-light: #6fb6c6;
    --teal-mid: #2f7f92;
    --teal-deep: #12394a;
    --night: #0b1a22;
    --glass: #7e9a98;
    --lawn: #3f6a52;
    --ink-light: #f2f7f8;
    --ink-soft: #e4ecee;
    --poems: #a9b4b6;
    --label: #6d6d6d;
  }
  html, body {
    margin: 0;
    width: 1200px;
    height: 918px;
    overflow: hidden;
    background: var(--page);
  }
  .spread {
    position: absolute;
    left: 45px;
    top: 43px;
    width: 1110px;
    height: 819px;
    overflow: hidden;
    background: var(--night);
  }
  .back-photo {
    position: absolute;
    inset: 0 auto 0 0;
    width: 600px;
    background:
      radial-gradient(ellipse 320px 520px at 130px 330px, rgba(134,202,231,0.55), transparent 70%),
      linear-gradient(90deg, var(--teal-light) 0%, var(--teal-mid) 38%, var(--teal-deep) 72%, var(--night) 100%);
  }
  .front-photo {
    position: absolute;
    left: 560px;
    top: 0;
    width: 550px;
    height: 819px;
    background:
      linear-gradient(180deg, transparent 0%, transparent 78%, var(--night) 100%),
      linear-gradient(180deg, #9fb4b1 0%, var(--glass) 35%, #748a86 62%, var(--lawn) 80%, #1a2e2c 100%);
  }
  .front-photo::before {
    content: "";
    position: absolute;
    inset: 0;
    background: linear-gradient(90deg, var(--night) 0%, rgba(11,26,34,0.4) 18%, transparent 40%, transparent 85%, rgba(11,26,34,0.7) 100%);
  }
  .blurb {
    position: absolute;
    left: 108px;
    top: 196px;
    width: 400px;
    margin: 0;
    text-align: center;
    font-family: "Sorts Mill Goudy", "Crimson Text", serif;
    font-size: 16px;
    line-height: 35.6px;
    color: var(--ink-light);
  }
  .blurb strong { font-family: "Crimson Text", serif; font-weight: 700; }
  .spine-text {
    position: absolute;
    left: 528px;
    writing-mode: vertical-rl;
    font-family: "Old Standard TT", serif;
    font-size: 11px;
    color: var(--ink-soft);
    white-space: nowrap;
  }
  .spine-title { top: 130px; letter-spacing: 11.5px; }
  .spine-author { top: 495px; letter-spacing: 6.8px; }
  .cover-title {
    position: absolute;
    right: 103px;
    top: 348px;
    margin: 0;
    text-align: right;
    font-family: "Old Standard TT", serif;
    font-weight: 400;
    color: var(--ink-light);
  }
  .cover-title .title { display: block; font-size: 25px; letter-spacing: 0.5px; line-height: 30px; }
  .cover-title .author { display: block; font-size: 17px; line-height: 22px; color: var(--ink-soft); }
  .cover-genre {
    position: absolute;
    right: 100px;
    top: 563px;
    margin: 0;
    font-family: "Sorts Mill Goudy", serif;
    font-style: italic;
    font-size: 33px;
    letter-spacing: 15px;
    color: var(--poems);
  }
  .spine-note {
    position: absolute;
    top: 874px;
    left: 0;
    width: 1128px;
    text-align: center;
    font-family: "Barlow", sans-serif;
    font-size: 16px;
    color: var(--label);
  }
</style>
</head>
<body>
  <div class="spread">
    <div class="back-photo" role="img" aria-label="Photograph of rain droplets on fogged blue glass"></div>
    <div class="front-photo" role="img" aria-label="Photograph looking out through a rain-streaked sash window at a country house and lawn"></div>

    <p class="blurb">
      <strong>The Lanternfield</strong> is a collection of poetry<br>
      documenting the lives of an aristocratic couple<br>
      throughout the 20th Century. Told in two parts<br>
      we first meet Charles – aged, crippled and left<br>
      alone in his inherited Marsh House - reflecting<br>
      on his life and his marriage to beautiful Alice<br>
      who we meet in part two. Alice is suicidal,<br>
      manically depressed and struggling with societal<br>
      conventions and life as a wife and mother.<br>
      She meets, harbors and falls in love with a soldier<br>
      during WWII and her world is changed forever.<br>
      Moving through decades, through this life and<br>
      the next - The Lanternfield interweaves themes of<br>
      grief, loss, the after-life, mental illness,<br>
      and ultimately the true nature of love.
    </p>

    <span class="spine-text spine-title">THE LANTERNFIELD</span>
    <span class="spine-text spine-author">Dorian Welkbridge</span>

    <h1 class="cover-title">
      <span class="title">THE LANTERNFIELD</span>
      <span class="author">Dorian Welkbridge</span>
    </h1>
    <p class="cover-genre">Poems</p>
  </div>
  <div class="spine-note">Spine = 0.2 Inch</div>
</body>
</html>
```